Label for a bottle of Gin soon to launch in the UK.

We need a label for a gin called Marbury Gin. It is very important that the label does not infringe any copyrights of the football club so please avoid the colour blue or anything related to football or the club. The example bottle below shows the bottle that we will be using. The gin will be clear not pink, the use of gold on the label is encouraged.
Should not infringe on the brand shown in the example image.

Industry/Entity Type

Club

Font styles to use
Sans Serif

Requirements
Must have
• Here is a link to the bottle that the label must fit onto https://www.vessel-depot-example.co.uk/Glass-bottles/Glass-bottles/700ml-glass-bottles/700ml-clear-glass-bottle-Quilora.html
Should not have
• No use of blue or anything related to football or Halcombe Rowing Society or Stonewrens. Avoid Red also. White, gold and black should be primary colours used

```html
<!DOCTYPE html>
<html lang="en">
<head>
<meta charset="utf-8">
<title>Marbury Gin – Bottle Label</title>
<link rel="stylesheet" href="https://fonts.googleapis.com/css2?family=Open+Sans:wght@400;700&display=swap">
<style>
  :root {
    --page-bg: #ffffff;
    --field-light: #fbf6e9;
    --field-gold: #c9a24a;
    --field-dark: #141414;
    --badge-centre: #ffffff;
    --badge-mid: #efe2bd;
    --badge-edge: #b8913c;
    --badge-rule: #ffffff;
    --ink: #111111;
  }
  html, body {
    margin: 0;
    padding: 0;
    width: 742px;
    height: 1200px;
    overflow: hidden;
    background: var(--page-bg);
  }
  .canvas {
    position: relative;
    width: 742px;
    height: 1200px;
  }
  .label {
    position: absolute;
    left: 155px;
    top: 478px;
    width: 435px;
    height: 467px;
  }
  .label-art {
    display: block;
    width: 100%;
    height: 100%;
  }
  .brand-name {
    font-family: "Open Sans", sans-serif;
    font-weight: 400;
    font-size: 28px;
    fill: var(--ink);
  }
  .product-type {
    font-family: "Open Sans", sans-serif;
    font-weight: 700;
    font-size: 30px;
    fill: var(--ink);
  }
</style>
</head>
<body>
<main class="canvas">
  <div class="label">
    <svg class="label-art" viewBox="0 0 435 467" xmlns="http://www.w3.org/2000/svg">
      <defs>
        <linearGradient id="wave-field-tone" x1="0" y1="0" x2="1" y2="1">
          <stop offset="0" stop-color="var(--field-light)"/>
          <stop offset="0.5" stop-color="var(--field-gold)"/>
          <stop offset="1" stop-color="var(--field-dark)"/>
        </linearGradient>
        <radialGradient id="badge-tone" cx="0.52" cy="0.6" r="0.6">
          <stop offset="0" stop-color="var(--badge-centre)"/>
          <stop offset="0.55" stop-color="var(--badge-mid)"/>
          <stop offset="1" stop-color="var(--badge-edge)"/>
        </radialGradient>
      </defs>

      <rect class="wave-field" x="0" y="0" width="435" height="467"
            fill="url(#wave-field-tone)" role="img"
            aria-label="Flowing pattern of fine diagonal wavy lines across the label"/>

      <g class="name-badge">
        <polygon points="227,0 405,127 227,257 50,127" fill="url(#badge-tone)"/>
        <polygon points="227,22 374,127 227,235 81,127" fill="none"
                 stroke="var(--badge-rule)" stroke-width="2" opacity="0.85"/>
        <text class="brand-name" x="205" y="137" text-anchor="middle">Marbury</text>
        <text class="product-type" x="212" y="194" text-anchor="middle">GIN</text>
      </g>
    </svg>
  </div>
</main>
</body>
</html>
```